New business blog needs wordpress theme

I need a unique wordpress theme for my new business oriented blog at quietharlan.net. The blog focuses on my experience as an entrepreneur and offers insights into business problems while chronicling my experience building a new company.

I would like to see a theme that looks more like a creative professional's website, not a business website. Large photos, bright colors, unique layout. I do not want stock photos of people in suits doing business type things. Also, no pictures of me - I am blogging anonymously.

The design should communicate technology and beauty - for example, I really like the feel of the landing page at www.plovel.com - it is beautiful to look at but also reflects the cutting edge nature of what they are doing.

Industry/Entity Type

Business

```html
<!DOCTYPE html>
<html lang="en">
<head>
<meta charset="utf-8">
<title>quietharlan — Blog Post</title>
<link rel="stylesheet" href="https://fonts.googleapis.com/css2?family=Open+Sans:wght@400;600;700&family=PT+Sans:wght@400;700&display=swap">
<style>
  :root {
    --hero-wood: #6a3a18;
    --hero-wood-deep: #3b2110;
    --hero-dark: #141613;
    --hero-shirt: #4e74b4;
    --hero-paper: #bfc2c2;
    --text-light: #ffffff;
    --nav-bg: rgba(36, 36, 36, 0.74);
    --scroll-bg: rgba(80, 80, 80, 0.8);
    --accent-bronze: #a66d2c;
    --search-bg: #fafafa;
    --search-icon: #9a9a9a;
    --social-icon: #e6e6e6;
  }
  * { box-sizing: border-box; margin: 0; padding: 0; }
  html, body {
    width: 1200px; height: 622px; overflow: hidden;
    background: var(--hero-dark);
    font-family: "Open Sans", sans-serif;
    color: var(--text-light);
  }
  .hero {
    position: relative; width: 1200px; height: 622px; overflow: hidden;
  }
  .hero-photo {
    position: absolute; inset: 0;
    background:
      radial-gradient(ellipse 260px 200px at 960px 150px, rgba(78,116,180,0.75), rgba(78,116,180,0) 100%),
      radial-gradient(ellipse 200px 260px at 230px 330px, rgba(191,194,194,0.45), rgba(191,194,194,0) 100%),
      radial-gradient(ellipse 220px 150px at 540px 500px, rgba(170,172,174,0.45), rgba(170,172,174,0) 100%),
      radial-gradient(ellipse 420px 380px at 160px 520px, rgba(106,58,24,0.9), rgba(106,58,24,0) 100%),
      linear-gradient(118deg, var(--hero-wood-deep) 0%, #2a1a10 35%, var(--hero-dark) 60%, #1b2638 100%);
  }
  .social-links {
    position: absolute; left: 154px; top: 36px;
    display: flex; gap: 22px; list-style: none;
  }
  .social-links li {
    width: 11px; height: 11px; border-radius: 50%;
    background: var(--social-icon);
  }
  .search-box {
    position: absolute; left: 765px; top: 19px;
    width: 231px; height: 29px;
    background: var(--search-bg);
  }
  .search-box svg { position: absolute; right: 8px; top: 7px; }
  .site-title {
    position: absolute; left: 0; right: 0; top: 96px;
    text-align: center;
    font-size: 48px; font-weight: 700; letter-spacing: 0.5px;
    line-height: 1;
  }
  .main-nav {
    position: absolute; left: 201px; top: 198px;
    width: 804px; height: 50px;
    background: var(--nav-bg);
  }
  .main-nav ul { list-style: none; position: relative; height: 100%; }
  .main-nav li {
    position: absolute; top: 0; height: 50px; line-height: 50px;
    font-family: "PT Sans", sans-serif;
    font-size: 17px; font-weight: 400; transform: translateX(-50%);
    white-space: nowrap;
  }
  .main-nav li.is-current { font-weight: 700; }
  .main-nav li svg { margin-left: 5px; vertical-align: middle; }
  .page-label {
    position: absolute; left: 451px; top: 296px;
    width: 276px; height: 60px;
    border: 2px solid var(--accent-bronze);
    text-align: center; line-height: 56px;
    font-size: 29px; font-weight: 600; letter-spacing: 1.5px;
  }
  .scroll-down {
    position: absolute; left: 529px; top: 542px;
    width: 125px; height: 50px;
    background: var(--scroll-bg);
    text-align: center;
    font-family: "PT Sans", sans-serif;
    font-size: 16px; line-height: 1;
    padding-top: 10px;
  }
  .scroll-down svg { display: block; margin: 3px auto 0; }
</style>
</head>
<body>
<header class="hero">
  <div class="hero-photo" role="img" aria-label="Overhead photo of a person working on a laptop at a wooden desk beside open books"></div>

  <ul class="social-links" aria-label="Social profiles">
    <li></li><li></li><li></li><li></li><li></li><li></li><li></li><li></li>
  </ul>

  <form class="search-box" role="search">
    <svg width="14" height="14" viewBox="0 0 14 14" aria-hidden="true">
      <circle cx="5.5" cy="5.5" r="4.2" fill="none" stroke="var(--search-icon)" stroke-width="1.8"/>
      <line x1="8.6" y1="8.6" x2="12.8" y2="12.8" stroke="var(--search-icon)" stroke-width="2.2" stroke-linecap="round"/>
    </svg>
  </form>

  <h1 class="site-title">quietharlan</h1>

  <nav class="main-nav">
    <ul>
      <li style="left:42px">HOME</li>
      <li class="is-current" style="left:150px">POST<svg width="10" height="7" viewBox="0 0 10 7" aria-hidden="true"><polyline points="1,1 5,5 9,1" fill="none" stroke="#fff" stroke-width="2"/></svg></li>
      <li style="left:281px">SMALL BUSINESS</li>
      <li style="left:457px">TECHNOLOGY</li>
      <li style="left:608px">ABOUT</li>
      <li style="left:752px">CONTACT</li>
    </ul>
  </nav>

  <div class="page-label">BLOG POST</div>

  <div class="scroll-down">SCROLL DOWN
    <svg width="20" height="12" viewBox="0 0 20 12" aria-hidden="true"><polyline points="2,2 10,9 18,2" fill="none" stroke="#fff" stroke-width="3.5"/></svg>
  </div>
</header>
</body>
</html>
```